Packaging Design for a Bakery Shop

We are opening a Bakery Shop in the Kingdom of Bahrain where we are going to sell bread items, Cakes, sweets, etc..and we have already selected the name and the logo design (check file named Crumvela to see the logo) .

We are looking to obtain designs for our packaging mainly the following (to see the plain sample items to be used for designing see the attached files with the same names):

1. Cake Box.
2. Pastry Box.
3. Brown bakery bags.
4. White bakery bags.
5. White nylon bags.
6. Toast transparent nylon bag.
7. Coffee paper cup.
8. Napkin.
9. Stickers (this should be a sticker to be used for packaging items that can not be printable so we can use the stickers instead).

Note that priority is for the cake box and the others can have the similar theme. So for designing the above, you are kindly requested to use a base similar to the attached files not other cuts. The designer may start his submission by applying the design on the cake box.

The theme to be designed by the designer should take into consideration the fact that the colours to be used shall be matching for sweets and breads. Also as you can see in the attached logo design it is kind of mid to high product price so the theme shall match with this level.

Also the designer shall bear in mind that we want a packaging design that is easy to apply and cost effective. Maximum colours to be used for packaging should be 3 colours only.

Note that the logo colour is still not defined, so you need also to change the logo colour to make it matching with the packaging.

Regards
Tariq Hallami
+973 36412258

Target Market(s)

It is mainly women since they are the one going mainly for the bakeries. Customers are mainly walking in customers.

Industry/Entity Type

Bakery

Font styles to use
Decorative

Requirements
Must have
• The design should be unique having a new idea and not same as others.
• The design should be cost effective and can be applied in all packaging in the bakery.
• In the design we need to have some part for the instgram, tweeter, phone icons.
• It should be suitable for both bread items and sweet items.
Should not have
• No more than 3 colours design

```html
<!DOCTYPE html>
<html lang="en">
<head>
<meta charset="utf-8">
<title>Crumvela Cake Box Dieline</title>
<link href="https://fonts.googleapis.com/css2?family=Playfair+Display:wght@500&family=Pinyon+Script&display=swap" rel="stylesheet">
<style>
  :root {
    --paper: #ffffff;
    --cream: #f3e6dc;
    --stripe: #f6ecdd;
    --brand: #a8927c;
    --icon: #d5bbab;
    --fold: #d9c2b6;
    --ink: #9a7f6c;
  }
  html, body {
    margin: 0;
    width: 1200px;
    height: 1200px;
    overflow: hidden;
    background: var(--paper);
  }
  .dieline {
    position: relative;
    width: 1200px;
    height: 1200px;
  }
  .side-flap {
    position: absolute;
    top: 300px;
    height: 596px;
    background: var(--cream);
    box-shadow: 0 0 24px rgba(232, 212, 196, 0.7);
  }
  .side-flap--left { left: 0; width: 300px; }
  .side-flap--right { left: 898px; width: 302px; }
  .main-panel {
    position: absolute;
    left: 300px;
    top: 0;
    width: 598px;
    height: 1200px;
    border-radius: 0 0 180px 180px;
    background: repeating-linear-gradient(90deg,
      var(--paper) 0 12px, var(--stripe) 12px 24px, var(--paper) 24px 30px);
    box-shadow: 0 0 22px rgba(232, 212, 196, 0.6);
    overflow: hidden;
  }
  .fold-line {
    position: absolute;
    border-color: var(--fold);
    border-style: dashed;
    border-width: 0;
  }
  .fold-line--h { left: 0; width: 1200px; border-top-width: 1px; }
  .fold-line--v { top: 0; height: 1180px; border-left-width: 1px; }
  .contact-icons {
    position: absolute;
    top: 40px;
    left: 518px;
    display: flex;
    gap: 20px;
  }
  .contact-icon {
    width: 40px;
    height: 40px;
    border-radius: 5px;
    background: var(--icon);
    display: flex;
    align-items: center;
    justify-content: center;
  }
  .address {
    position: absolute;
    left: 300px;
    width: 598px;
    top: 110px;
    text-align: center;
    transform: rotate(180deg);
    font-family: "Pinyon Script", cursive;
    font-size: 13px;
    line-height: 18px;
    color: var(--ink);
    margin: 0;
  }
  .brand {
    position: absolute;
    left: 300px;
    width: 598px;
    height: 160px;
    display: flex;
    align-items: center;
    justify-content: center;
    gap: 14px;
    background: radial-gradient(ellipse at center, rgba(255,255,255,0.95) 0 35%, rgba(255,255,255,0) 70%);
  }
  .brand--front { top: 710px; }
  .brand--lid { top: 965px; }
  .brand__dot {
    width: 12px;
    height: 12px;
    border-radius: 50%;
    background: var(--brand);
  }
  .brand__name {
    font-family: "Playfair Display", serif;
    font-weight: 500;
    font-size: 64px;
    color: var(--brand);
  }
</style>
</head>
<body>
<main class="dieline">
  <div class="side-flap side-flap--left"></div>
  <div class="side-flap side-flap--right"></div>
  <div class="main-panel"></div>

  <div class="fold-line fold-line--h" style="top:300px"></div>
  <div class="fold-line fold-line--h" style="top:896px"></div>
  <div class="fold-line fold-line--v" style="left:300px"></div>
  <div class="fold-line fold-line--v" style="left:898px"></div>

  <div class="contact-icons">
    <div class="contact-icon" aria-label="Social account"></div>
    <div class="contact-icon" aria-label="Social account"></div>
    <div class="contact-icon" aria-label="Phone">
      <svg width="22" height="22" viewBox="0 0 24 24"><path fill="#fff" d="M6.6 10.8a15.1 15.1 0 0 0 6.6 6.6l2.2-2.2c.3-.3.7-.4 1-.2 1.1.4 2.3.6 3.6.6.6 0 1 .4 1 1V20c0 .6-.4 1-1 1C10.6 21 3 13.4 3 4c0-.6.4-1 1-1h3.5c.6 0 1 .4 1 1 0 1.3.2 2.5.6 3.6.1.3 0 .7-.2 1z"/></svg>
    </div>
  </div>

  <p class="address">address address address address address address address address<br>address address address address address</p>

  <div class="brand brand--front">
    <span class="brand__dot"></span>
    <span class="brand__name">Crumvela</span>
  </div>
  <div class="brand brand--lid">
    <span class="brand__dot"></span>
    <span class="brand__name">Crumvela</span>
  </div>
</main>
</body>
</html>
```